History Wall Typography -- Vela Coffee family history

I have text and photos to be represented as one large wall art piece. Its a coffee business going back to 1894. Family Names, Dates birth/death, Occupation, photo of husband and wife and the photo of coffee brand at the time. All in the same font colour style of the branding. Example typography attached but can be a different shape.

Family Dorn and Mabela Koffie timeline - 5 generations of coffee - in Dutch

1st Generatie :
Evaristus Dorn – Geboren:1846 - Plaats: Brakel - Bezetting: Koffiehandleer
Wife - Bernadette Van Der Molen – Geboren: 1845

2nd Generatie - Broers
Lucien Dorn Geboren: 1884 Plaats: Geraardsbergen Bezetting: Koffiehandler
Wife of Lucien: Edith Vermaelen Geboren: 1883
Achiel Dorn - Geboren:? - Plaats: Geraardsbergen Bezetting: Koffiehandler /Architect
Wife of Achiel: Wouterse Dorn Geboren

3rd Generation - Cousins
Marcel August Dorn (Son of Lucien) - Geboren: 1923 - Plaats: Geraardsbergen -Bezetting: Café Owner & Koffiehandler
Wife of Marcel: Clara Henrietta Van Der Poel(Lotte) Geboren: 1923 - Bezetting: Café Owner & Koffiehandler
Hugo Dorn (Son on Achiel) – Geboren: 1921 – Plaats: Geraardsbergen - Bezetting: Koffiehandler/Lid van Armed Resistance
Wife of Hugo: Leonie Margot Camiel Vranckaert

4th Generatie:
Bruno Dorn - Geboren:1953 - Plaats: Geraardsbergen- Bezetting: Director at GROEP HEILIG-ANSELMUS /Koffiehandler
Veronique Van Kerckhoven - Geboren: 1955 - Plaats: Geraardsbergen - Bezetting: Café Owner & Koffiehandler

5th Generatie:- Broers
Damien Dorn: Geboren::1979 - Plaats:: Geraardsbergen -Bezetting: Koffiehandler/Geluids ingenieur
Thibaut Dorn: Geboren::1981 - Plaats:: Geraardsbergen -Bezetting: Koffiehandler/Sales Director
Updates

Hi, Can you please extend this I only approved the guy to work on the project and he has yet to deliver anything. Thanks, Beatrix

Target Market(s)

Coffee lovers artisanal coffee

Industry/Entity Type

Professional Service

Font styles to use
Other font styles liked:
• universal_Serif, Caniste font family, sen

Colors

Designer to choose colors to be used in the design.

Requirements
Must have
• The project must include a time wall with font and branding of logo (attached) The family members, dates, occupation, address , photo of them and picture of the coffee brand at that time should be included.
Nice to have
• See invite to Launch party for style that could work

one large wall but a pillar in the middle. I'll upload the picture of the wall. The picture can go up and down it does not have to be one line. the Horizontal wall is 160cm one side, pillar is 46cm with 10.5cm each side of pillar. The second wall is 160cm too. The vertical dimensions is 180cm. The picture does not have to be full size but something that fits in well.
Should not have
• Should not be plain or like the bad example attached. it should be like the launch party colours and fonts

```html
<!DOCTYPE html>
<html lang="nl">
<head>
<meta charset="utf-8">
<title>Vijf Generaties Koffie – Mabela Coffee</title>
<link rel="stylesheet" href="https://fonts.googleapis.com/css2?family=Roboto+Slab:wght@800&family=Barlow:wght@400;500&family=Barlow+Semi+Condensed:wght@500&display=swap">
<style>
  :root {
    --parchment-light: #dccaa8;
    --parchment-mid: #cdb893;
    --parchment-dark: #a8916c;
    --ink: #5b3b1f;
    --ink-soft: #6a4a2c;
    --frame: #5a3719;
    --title-shadow: #b89f79;
  }
  * { margin: 0; padding: 0; box-sizing: border-box; }
  html, body { width: 1200px; height: 800px; overflow: hidden; }
  body { background: var(--parchment-mid); }
  .wall {
    position: relative;
    width: 1200px; height: 800px;
    overflow: hidden;
    background:
      radial-gradient(ellipse at 50% 45%, rgba(236,222,196,0.85) 0%, rgba(220,202,168,0.4) 45%, rgba(150,125,90,0.45) 100%),
      linear-gradient(160deg, var(--parchment-light), var(--parchment-mid) 60%, var(--parchment-dark));
    color: var(--ink);
    font-family: "Barlow", sans-serif;
  }
  .wall__title {
    position: absolute; left: 200px; width: 760px; top: 30px;
    text-align: center; white-space: nowrap;
    font-family: "Roboto Slab", serif; font-weight: 800;
    font-size: 58px; letter-spacing: 1.5px;
    color: var(--ink);
    text-shadow: 3px 3px 0 var(--title-shadow);
    line-height: 1;
  }
  .brand {
    position: absolute; left: 1014px; top: 28px; width: 160px;
    display: flex; align-items: center; gap: 8px;
    font-family: "Barlow", sans-serif; font-weight: 500;
    color: var(--ink); line-height: 1.1;
  }
  .brand__dot { width: 14px; height: 14px; border-radius: 50%; background: var(--ink); flex: none; }
  .brand__name { font-size: 28px; letter-spacing: 1px; display: block; }
  .brand__sub { font-size: 13px; letter-spacing: 3px; display: block; }
  .portrait {
    position: absolute; width: 145px; height: 172px;
    border: 10px solid var(--frame);
  }
  .portrait--vintage { background: linear-gradient(160deg, #d9d9d6, #9c9c98 60%, #5e5e5a); }
  .portrait--sepia { background: linear-gradient(160deg, #e4ddd0, #8f8273 55%, #3b3128); }
  .portrait--mono { background: linear-gradient(150deg, #e2e2e2, #8a8a8a 50%, #2e2e2e); }
  .portrait--colour { background: linear-gradient(150deg, #8a7060, #4b3a30 50%, #1c1714); }
  .generation { position: absolute; white-space: nowrap; }
  .generation__heading {
    font-family: "Barlow Semi Condensed", sans-serif; font-weight: 500;
    font-size: 25px; color: var(--ink); line-height: 1;
    margin-bottom: 12px;
  }
  .generation__text {
    font-size: 17.5px; line-height: 20px; color: var(--ink-soft);
  }
  .generation__text--dense { font-size: 16px; line-height: 19px; }
</style>
</head>
<body>
<main class="wall">
  <h1 class="wall__title">VIJF GENERATIES KOFFIE</h1>

  <div class="brand"><span class="brand__dot"></span><span><span class="brand__name">MABELA</span><span class="brand__sub">COFFEE</span><span class="brand__sub">FAM. DORN</span></span></div>

  <div class="portrait portrait--vintage" style="left:43px;top:118px" role="img" aria-label="Portret van Evaristus Dorn, eerste generatie"></div>
  <section class="generation" style="left:215px;top:158px">
    <h2 class="generation__heading">1st Generatie :</h2>
    <p class="generation__text">Evaristus Dorn – Geboren:<br>1846 – Plaats: Brakel –<br>Bezetting: Koffiehandleer<br>Wife – Bernadette Van Der Molen –<br>Geboren: 1845</p>
  </section>

  <div class="portrait portrait--mono" style="left:45px;top:345px" role="img" aria-label="Portret van Lucien Dorn, tweede generatie"></div>
  <section class="generation" style="left:215px;top:345px">
    <h2 class="generation__heading">2nd Generatie - Broers</h2>
    <p class="generation__text">Lucien Dorn Geboren: 1884 Plaats:<br>Geraardsbergen Bezetting: Koffiehandler<br>Wife of Lucien: Edith Vermaelen Geboren: 1883<br>Achiel Dorn – Geboren:? – Plaats:<br>Geraardsbergen Bezetting: Koffiehandler<br>/Architect<br>Wife of Achiel: Wouterse Dorn Geboren</p>
  </section>

  <div class="portrait portrait--sepia" style="left:43px;top:578px;height:176px" role="img" aria-label="Portret van Marcel August Dorn, derde generatie"></div>
  <section class="generation" style="left:215px;top:575px">
    <h2 class="generation__heading">3rd Generation - Cousins</h2>
    <p class="generation__text generation__text--dense">Marcel August Dorn (Son of Lucien) – Geboren: 1923 – Plaats:<br>Geraardsbergen –Bezetting: Café Owner &amp; Koffiehandler<br>Wife of Marcel: Clara Henrietta Van Der Poel(Lotte) Geboren:<br>1923 – Bezetting: Café Owner &amp; Koffiehandler<br>Hugo Dorn (Son on Achiel) – Geboren: 1921 – Plaats:<br>Geraardsbergen – Bezetting: Koffiehandler/Lid van Armed<br>Resistance<br>Wife of Hugo: Leonie Margot Camiel Vranckaert</p>
  </section>

  <div class="portrait portrait--mono" style="left:695px;top:216px" role="img" aria-label="Foto van Bruno Dorn en Veronique Van Kerckhoven, vierde generatie"></div>
  <section class="generation" style="left:862px;top:218px">
    <h2 class="generation__heading">4th Generatie:</h2>
    <p class="generation__text" style="font-size:17px">Bruno Dorn – Geboren:1953 – Plaats:<br>Geraardsbergen– Bezetting: Director at<br>GROEP HEILIG-ANSELMUS<br>/Koffiehandler<br>Veronique Van Kerckhoven – Geboren:<br>1955 – Plaats: Geraardsbergen –<br>Bezetting: Café Owner &amp; Koffiehandler</p>
  </section>

  <div class="portrait portrait--colour" style="left:695px;top:498px" role="img" aria-label="Foto van de broers Damien en Thibaut Dorn, vijfde generatie"></div>
  <section class="generation" style="left:862px;top:498px">
    <h2 class="generation__heading" style="margin-bottom:31px">5th Generatie:- Broers</h2>
    <p class="generation__text" style="font-size:17px">Damien Dorn: Geboren::1979 – Plaats::<br>Geraardsbergen –Bezetting:<br>Koffiehandler/Geluids ingenieur<br>Thibaut Dorn: Geboren::1981 – Plaats::<br>Geraardsbergen –Bezetting:<br>Koffiehandler/Sales Director</p>
  </section>
</main>
</body>
</html>
```